Visitenkarten-Design für Catering/ Liefertouren
Vielen Dank für die professionelle Zusammenarbeit. Änderungen wurden schnell und treffend umgesetzt. Wir sind mit dem Ergebnis sehr zufrieden.
Zielgruppe
Catering/ Liefertouren für hochwertige selbstgemachte Quiches/ französische Tartes, Suppen, Currys
Aufgabenstellung
2 Visitenkarten im Format DIN6 (21x10,5) lang die sich auf der 1. (Bild) Seite unterscheiden aber mit identischer 2. Seite.
Karte 'Quiche' 1. Seite:
'Quiche '
Quiche Passion - depuis 2003
Quiches, Soups, Currys,
Catering, Abholung, Liefertouren
www.Kovendo.de,
info@kovendo.de
Karte 'Soups' 1. Seite:
'KovendoChicken, KovendoTofu'
2. Seite (für beide Karten identisch)
Seite soll eine Art Vorlage sein und besteht lediglich aus einer gestalterischen 'Umrahmung' und unserem Logo am unteren Seitenrand. Der Durchmesser des Logos soll max. 15% der gesamten Seitenlänge betragen.
Seite wird von uns mit Angeboten/ Aktionen bedruckt in kleiner Stückzahl nachträglich bedruckt.
1. Seiten (Quer- oder Hochformat je nach Bild möglich).
2. Seite im Hochformat.
Keine Vorgaben bzgl. Schrifttyp.

```html
<!DOCTYPE html>
<html lang="de">
<head>
<meta charset="utf-8">
<title>Kovendo – Visitenkarten</title>
<link href="https://fonts.googleapis.com/css2?family=Alegreya:wght@400;500&display=swap" rel="stylesheet">
<style>
  :root {
    --stage: #e6e6e8;
    --brown: #40231f;
    --brown-soft: #6b4f4a;
    --paper: #ffffff;
    --text-light: #f4ece6;
    --shadow: rgba(0,0,0,0.18);
  }
  * { margin: 0; padding: 0; box-sizing: border-box; }
  html, body { width: 1200px; height: 767px; overflow: hidden; }
  body {
    background: var(--stage);
    font-family: "Alegreya", Georgia, serif;
    position: relative;
  }
  .card-front {
    position: absolute;
    left: 31px;
    width: 667px;
    height: 333px;
    background: var(--brown-soft);
    box-shadow: 0 1px 3px var(--shadow);
    overflow: hidden;
  }
  .card-front--quiche { top: 37px; }
  .card-front--soups { top: 398px; }

  .service-bar {
    position: absolute; left: 0; top: 0; width: 100%; height: 29px;
    background: var(--brown);
    color: var(--text-light);
    font-size: 15px;
    letter-spacing: 0.3px;
    display: flex; align-items: center; justify-content: center;
  }
  .hero {
    position: absolute; left: 0; top: 32px; width: 100%; height: 250px;
  }
  .card-front--quiche .hero {
    background:
      radial-gradient(circle 225px at 345px 110px,
        #8a8a4c 0%, #6f7540 45%, #5d6634 72%, #b9915a 88%, rgba(70,70,60,0.6) 96%, rgba(0,0,0,0) 100%),
      linear-gradient(90deg, #3b4d72 0%, #334463 35%, #26304a 70%, #1b2030 100%);
  }
  .card-front--soups .hero {
    background:
      radial-gradient(circle 80px at 370px 120px, #c4502e 0%, #a83c22 65%, #2b2928 88%, rgba(40,40,40,0) 100%),
      radial-gradient(circle 150px at 370px 120px, #3a3836 0%, #4a4744 70%, rgba(0,0,0,0) 100%),
      linear-gradient(90deg, #4f9140 0%, #3f7a35 22%, #5a5550 40%, #45413d 62%, #3f7432 78%, #5a9a3f 100%);
  }
  .hero::before, .hero::after {
    content: ""; position: absolute; left: 0; width: 100%; height: 30px;
    background: rgba(255,255,255,0.2);
  }
  .hero::before { top: 0; }
  .hero::after { bottom: 0; }

  .hero-title {
    position: absolute;
    color: #fff;
    font-weight: 400;
    font-size: 80px;
    line-height: 1;
    text-shadow: 0 2px 8px rgba(0,0,0,0.5);
  }
  .hero-tagline {
    position: absolute;
    color: #fff;
    font-size: 14px;
    text-shadow: 0 1px 3px rgba(0,0,0,0.6);
  }
  .card-front--quiche .hero-title { left: 34px; top: 108px; }
  .card-front--quiche .hero-tagline { left: 91px; top: 180px; }
  .card-front--soups .hero-title { left: 41px; top: 108px; }
  .card-front--soups .hero-tagline { left: 46px; top: 199px; }

  .contact-bar {
    position: absolute; left: 0; bottom: 0; width: 100%; height: 44px;
    background: var(--brown);
    color: var(--text-light);
    font-size: 15.5px;
    letter-spacing: 0.3px;
    display: flex; align-items: center; justify-content: center;
  }
  .contact-item { padding: 0 17px; }
  .contact-divider { width: 1px; height: 26px; background: var(--text-light); opacity: 0.8; }

  .card-back {
    position: absolute; left: 782px; top: 37px;
    width: 349px; height: 695px;
    background: var(--paper);
    box-shadow: 0 1px 3px var(--shadow);
  }
  .card-back svg { position: absolute; left: 0; top: 0; }
  .ghost-name {
    position: absolute; left: 0; top: 270px; width: 100%;
    text-align: center;
    font-size: 60px;
    color: #f3f3f3;
  }
  .brand-seal {
    position: absolute; left: 126px; top: 551px;
    width: 108px; height: 108px; border-radius: 50%;
    background: var(--brown);
    display: flex; align-items: center; justify-content: center;
    color: #fff; font-size: 22px;
  }
</style>
</head>
<body>

<section class="card-front card-front--quiche">
  <div class="service-bar">Quiches | Soups | Currys | Catering | Abholung | Liefertouren</div>
  <div class="hero" role="img" aria-label="Foto einer Spinat-Quiche mit Tortenheber auf dunkelblauem Untergrund">
    <h2 class="hero-title">Quiche</h2>
    <p class="hero-tagline">Quiche Passion - depuis 2003</p>
  </div>
  <div class="contact-bar">
    <span class="contact-item">www.kovendo.de</span>
    <span class="contact-divider"></span>
    <span class="contact-item">+49 (0) 89-7140 2285</span>
    <span class="contact-divider"></span>
    <span class="contact-item">info@kovendo.de</span>
  </div>
</section>

<section class="card-front card-front--soups">
  <div class="service-bar">Quiches | Soups | Currys | Catering | Abholung | Liefertouren</div>
  <div class="hero" role="img" aria-label="Foto einer Tomatensuppe mit Croûtons im Gusstopf, umgeben von Kräutern und Zwiebeln">
    <h2 class="hero-title">Soups</h2>
    <p class="hero-tagline">Quiche Passion - depuis 2003</p>
  </div>
  <div class="contact-bar">
    <span class="contact-item">www.kovendo.de</span>
    <span class="contact-divider"></span>
    <span class="contact-item">+49 (0) 89-7140 2285</span>
    <span class="contact-divider"></span>
    <span class="contact-item">info@kovendo.de</span>
  </div>
</section>

<section class="card-back">
  <svg width="349" height="695" viewBox="0 0 349 695" aria-hidden="true">
    <path d="M18 614 V36 Q18 18 36 18 H317 Q335 18 335 36 V614"
          fill="none" stroke="#40231f" stroke-width="1.6"/>
    <path d="M0 614 Q60 606 126 614 M234 614 Q290 606 349 614"
          fill="none" stroke="#40231f" stroke-width="1.6"/>
  </svg>
  <div class="ghost-name">Kovendo</div>
  <div class="brand-seal">Kovendo</div>
</section>

</body>
</html>
```